Website Homepage Design for New Cosmetic Line

Design the Homepage for the website based on a provided Wireframe. Assets have been be provided for the design, with the expectation that the designer will provide the creative flair. Along with the homepage design, a list of site fonts and colours will also be needed for internal pages (but no internal page designs required. )
Layout/wireframe is here: http://verano-plumcosmetics.com/layout/ (and also attached in files as PNG and PDF)
No need to follow the Layout exactly as far as spacing and font go, just make sure all elements are on the page, and look amazing!
My Client gave these sites for comparable in the industry:
https://www.quorvabeauty.com/
https://www.marisoltenderwoodglow.com/ (does not like video in header though)

Moving Down the Wireframe:
Header Logo - Use the Text only from the logo, not the Circle at the top here
Navigation - Copy these items
Hero Image: Use the image stated. Feel free to add some creativity over it, make sure that the lips and product are still visible, and also that the Text that is being overlaid can be easily read
Arm Swatch and Lip Swatches, make them pop!
Featured Products, 2 of the images are in RAW from the photographer - you may want to convert them to jpg. Feel free to adjust if needed, for sizing and brightness. If you want to crop the images from the backgrounds, you could do that too to allow for more consistency.
Reviews show the needed content as well.

Footer speaks for itself - use the Full Round Logo here.

All Assets are here: https://files.stashbarn.net/folders/8kQwLmZ2xR4tYp9VnHc3JdE6sUb7aGo?usp=sharing

The main assets are also attached in a zip file, but there are more in the above shared link for additional creativity/resources

• Unique and Beautiful Design
Clear Layout
Follow Best Practices in Design layout for development (eg based on 12 grid)
Please Use Google Fonts

```html
<!DOCTYPE html>
<html lang="en">
<head>
<meta charset="utf-8">
<title>Verano Plum Cosmetics — Home</title>
<link href="https://fonts.googleapis.com/css2?family=Open+Sans:wght@400;600;700&family=Yesteryear&display=swap" rel="stylesheet">
<style>
:root{
  --pink:#ef7580;
  --pink-deep:#e35a68;
  --coral:#f06a72;
  --button:#ee5f6c;
  --brown:#5b4547;
  --ink:#333;
  --muted:#8a8a8a;
  --white:#fff;
  --mist:#f3eef4;
  --gold:#f3c27a;
}
*{box-sizing:border-box;margin:0;padding:0}
html,body{width:1200px;height:3636px;overflow:hidden}
body{font-family:"Open Sans",Arial,sans-serif;color:var(--ink);background:var(--white);position:relative}
section,header,footer{position:relative;width:1200px;overflow:hidden}
.script{font-family:"Yesteryear",cursive;font-weight:400}
.pattern{position:absolute;inset:0;background:radial-gradient(circle at 18% 30%,rgba(255,255,255,.16),rgba(255,255,255,0) 38%),radial-gradient(circle at 85% 75%,rgba(255,255,255,.14),rgba(255,255,255,0) 40%)}

/* Hero */
.hero{height:580px}
.hero-photo{position:absolute;inset:0;background:linear-gradient(100deg,#3a1e24 0%,#8b3a52 35%,#c9677f 55%,#6b2c3c 80%,#2a1519 100%)}
.hero-veil{position:absolute;inset:0;background:linear-gradient(180deg,rgba(0,0,0,.25),rgba(0,0,0,0) 25%,rgba(255,255,255,.15) 100%)}
.top-nav{position:absolute;top:0;left:0;right:0;height:40px;display:flex;justify-content:center;gap:28px;align-items:center;font-size:14px;color:var(--white)}
.hero-brand{position:absolute;left:440px;top:232px;display:flex;align-items:center;gap:14px;color:var(--white);font-size:32px;white-space:nowrap}
.brand-dot{width:14px;height:14px;border-radius:50%;background:var(--white)}
.hero-badge{position:absolute;left:545px;top:512px;width:110px;height:110px;border-radius:50%;background:var(--white);border:8px solid var(--pink);z-index:3}

/* Mission */
.mission{height:340px;background:linear-gradient(90deg,var(--mist),#fbf4f6 60%,#fff)}
.section-title{font-size:46px;color:var(--pink-deep);text-align:center}
.mission .section-title{position:absolute;top:60px;left:0;right:0}
.mission-text{position:absolute;top:140px;left:340px;width:520px;text-align:center;font-size:17px;line-height:1.6;color:var(--muted)}
.mission-photo{position:absolute;left:900px;top:120px;width:240px;height:200px;background:linear-gradient(160deg,#fdfdfd,#eee 60%,#d23548 62%,#2a2a2a 75%,#eee 80%)}

/* Swatches */
.swatches{height:1060px;background:linear-gradient(180deg,var(--coral),var(--pink) 60%,#f08a92)}
.swatch-photo{position:absolute;left:152px;top:60px;width:896px;height:560px;background:linear-gradient(180deg,#a78472 0%,#8a6a5c 50%,#ece6df 52%,#d8d0c8 100%)}
.swatches .section-title{position:absolute;top:710px;left:0;right:0;color:var(--white)}
.gallery{position:absolute;top:808px;left:148px;display:flex;gap:20px}
.gallery div{width:290px;height:172px;border:6px solid var(--white);background:linear-gradient(135deg,#e9a3a8,#b3414f 50%,#f5c1c6)}

/* Featured */
.featured{height:560px;background:var(--white)}
.featured .section-title{position:absolute;top:40px;left:0;right:0}
.product{position:absolute;top:132px;width:232px;text-align:center}
.product .shot{height:228px;border:1px solid #ddd}
.product h3{margin-top:50px;font-size:16px;font-weight:400;color:var(--pink-deep)}
.shop-btn{display:inline-flex;align-items:center;gap:8px;margin-top:14px;background:var(--button);color:var(--white);font-size:15px;padding:8px 22px;border-radius:2px}
.arrow{position:absolute;width:56px;height:56px}

/* Reviews */
.reviews{height:660px;background:linear-gradient(180deg,var(--pink),#ee6e79)}
.reviews .section-title{position:absolute;top:20px;left:0;right:0;color:var(--white)}
.avatar{position:absolute;left:500px;top:80px;width:200px;height:200px;border-radius:50%;border:8px solid var(--white);background:linear-gradient(160deg,#6b4434,#3a2520)}
.reviewer{position:absolute;top:318px;left:0;right:0;text-align:center;color:var(--white);font-size:18px}
.stars{position:absolute;top:356px;left:0;right:0;display:flex;justify-content:center;gap:4px}
.review-text{position:absolute;top:420px;left:200px;width:800px;text-align:center;color:rgba(255,255,255,.75);font-size:17px;line-height:1.65}
.review-count{position:absolute;top:560px;left:0;right:0;text-align:center;color:var(--white);font-size:13px}
.pager{position:absolute;top:600px;left:485px;width:230px;height:40px;background:#7a3e46;color:var(--white);display:flex;align-items:center;justify-content:center;gap:12px;font-size:15px}

/* Share */
.share{height:160px;text-align:center}
.share h4{padding-top:40px;font-size:20px;font-weight:700;letter-spacing:.5px}
.share-icons{display:flex;justify-content:center;gap:4px;margin-top:14px}
.share-icons span{width:26px;height:26px;background:#3d5a98;border-radius:2px}

/* Footer */
.site-footer{height:220px;background:var(--brown);color:var(--white)}
.footer-brand{position:absolute;left:130px;top:98px;display:flex;align-items:center;gap:10px;font-size:17px;white-space:nowrap}
.footer-brand .brand-dot{width:10px;height:10px}
.quick-links{position:absolute;left:400px;top:50px;font-size:14px;line-height:1.9}
.quick-links h5{font-size:16px;font-weight:600;color:var(--gold)}
.tagline{position:absolute;left:652px;top:20px;font-size:36px;white-space:nowrap}
.tagline em{font-family:"Open Sans",Arial,sans-serif;font-style:normal;font-size:28px}
.subscribe{position:absolute;left:652px;top:96px;display:flex;align-items:center;gap:12px;font-size:13px}
.subscribe .field{width:200px;height:30px;background:var(--white)}
.subscribe .go{background:var(--button);padding:6px 16px;font-size:13px}
.footer-social{position:absolute;left:852px;top:150px;display:flex;gap:10px}
.footer-social span{width:36px;height:36px;border-radius:50%;background:var(--white)}
.legal{height:56px;display:flex;justify-content:space-between;align-items:center;padding:0 40px;font-size:11px;color:var(--muted)}
</style>
</head>
<body>

<header class="hero">
  <div class="hero-photo" role="img" aria-label="Close-up of glossy pink lips with a liquid lipstick tube held beside them"></div>
  <div class="hero-veil"></div>
  <nav class="top-nav"><span>Home</span><span>About</span><span>Shop</span><span>Blog</span><span>Contact</span></nav>
  <div class="hero-brand"><span class="brand-dot"></span><span>Verano Plum Cosmetics</span></div>
  <div class="hero-badge" role="img" aria-label="Made in Canada badge"></div>
</header>

<section class="mission">
  <h2 class="section-title script">Our Mission</h2>
  <p class="mission-text">Verano Plum Cosmetics was created for inclusivity. An all Canadian brand inspired by the cultural mosaic we live in with colours unbound.</p>
  <div class="mission-photo" role="img" aria-label="Red lipstick bullet standing beside white flowers"></div>
</section>

<section class="swatches">
  <div class="pattern" role="img" aria-label="Soft lace mandala pattern in light pink"></div>
  <div class="swatch-photo" role="img" aria-label="Lip colour swatches printed on two arms of different skin tones"></div>
  <h2 class="section-title script">By Us For All</h2>
  <div class="gallery">
    <div role="img" aria-label="Lip palette open with pink and red shades"></div>
    <div role="img" aria-label="Lip palette shown in hand"></div>
    <div role="img" aria-label="Eye shadow palette close-up"></div>
  </div>
</section>

<section class="featured">
  <h2 class="section-title script">Featured Products</h2>
  <svg class="arrow" style="left:128px;top:196px" viewBox="0 0 56 56"><circle cx="28" cy="28" r="25" fill="#fff" stroke="#ee5f6c" stroke-width="4"/><circle cx="28" cy="28" r="18" fill="#ee5f6c"/><path d="M31 20l-8 8 8 8" fill="none" stroke="#fff" stroke-width="4"/></svg>
  <div class="product" style="left:220px">
    <div class="shot" role="img" aria-label="Liquid lipstick tube in red" style="background:linear-gradient(90deg,#fafafa 40%,#b3262f 45%,#b3262f 55%,#fafafa 60%)"></div>
    <h3>Liquid Lipstick</h3>
    <span class="shop-btn">Shop Now
      <svg width="18" height="16" viewBox="0 0 18 16"><path d="M1 1h3l2 9h9l2-7H5" fill="none" stroke="#fff" stroke-width="1.8"/><circle cx="7" cy="14" r="1.5" fill="#fff"/><circle cx="14" cy="14" r="1.5" fill="#fff"/></svg></span>
  </div>
  <div class="product" style="left:484px">
    <div class="shot" role="img" aria-label="Warm lip palette on a pink background" style="background:#e8577a;border-color:#e8577a"></div>
    <h3>Warm Lip Palette</h3>
    <span class="shop-btn">Shop Now
      <svg width="18" height="16" viewBox="0 0 18 16"><path d="M1 1h3l2 9h9l2-7H5" fill="none" stroke="#fff" stroke-width="1.8"/><circle cx="7" cy="14" r="1.5" fill="#fff"/><circle cx="14" cy="14" r="1.5" fill="#fff"/></svg></span>
  </div>
  <div class="product" style="left:748px">
    <div class="shot" role="img" aria-label="Sunset eye shadow palette with orange and pink pans" style="background:linear-gradient(135deg,#2b2b2b,#f08a4b 50%,#d8455b)"></div>
    <h3>Eye Shadow Sunset Palette</h3>
    <span class="shop-btn">Shop Now
      <svg width="18" height="16" viewBox="0 0 18 16"><path d="M1 1h3l2 9h9l2-7H5" fill="none" stroke="#fff" stroke-width="1.8"/><circle cx="7" cy="14" r="1.5" fill="#fff"/><circle cx="14" cy="14" r="1.5" fill="#fff"/></svg></span>
  </div>
  <svg class="arrow" style="left:1024px;top:196px" viewBox="0 0 56 56"><circle cx="28" cy="28" r="25" fill="#fff" stroke="#ee5f6c" stroke-width="4"/><circle cx="28" cy="28" r="18" fill="#ee5f6c"/><path d="M25 20l8 8-8 8" fill="none" stroke="#fff" stroke-width="4"/></svg>
</section>

<section class="reviews">
  <div class="pattern" role="img" aria-label="Soft lace mandala pattern in light pink"></div>
  <h2 class="section-title script">Reviews</h2>
  <div class="avatar" role="img" aria-label="Reviewer portrait"></div>
  <svg class="arrow" style="left:124px;top:262px" viewBox="0 0 56 56"><circle cx="28" cy="28" r="24" fill="none" stroke="#fff" stroke-width="3"/><path d="M31 20l-8 8 8 8" fill="none" stroke="#fff" stroke-width="4"/></svg>
  <svg class="arrow" style="left:1020px;top:262px" viewBox="0 0 56 56"><circle cx="28" cy="28" r="24" fill="none" stroke="#fff" stroke-width="3"/><path d="M25 20l8 8-8 8" fill="none" stroke="#fff" stroke-width="4"/></svg>
  <p class="reviewer">Liquid Lipstick</p>
  <div class="stars" aria-label="5 out of 5 stars">
    <svg width="22" height="22" viewBox="0 0 24 24"><path d="M12 2l3 7h7l-6 4.5 2.5 7.5L12 16l-6.5 5 2.5-7.5L2 9h7z" fill="#f6c343"/></svg>
    <svg width="22" height="22" viewBox="0 0 24 24"><path d="M12 2l3 7h7l-6 4.5 2.5 7.5L12 16l-6.5 5 2.5-7.5L2 9h7z" fill="#f6c343"/></svg>
    <svg width="22" height="22" viewBox="0 0 24 24"><path d="M12 2l3 7h7l-6 4.5 2.5 7.5L12 16l-6.5 5 2.5-7.5L2 9h7z" fill="#f6c343"/></svg>
    <svg width="22" height="22" viewBox="0 0 24 24"><path d="M12 2l3 7h7l-6 4.5 2.5 7.5L12 16l-6.5 5 2.5-7.5L2 9h7z" fill="#f6c343"/></svg>
    <svg width="22" height="22" viewBox="0 0 24 24"><path d="M12 2l3 7h7l-6 4.5 2.5 7.5L12 16l-6.5 5 2.5-7.5L2 9h7z" fill="#f6c343"/></svg>
  </div>
  <p class="review-text">This lip color is my everyday favourite. The formula is smooth and long lasting, and the shade flatters every skin tone I have tried it on. It never dries my lips and stays put from morning coffee through a late dinner with friends. Truly a staple.</p>
  <p class="review-count">1/20</p>
  <div class="pager"><span>‹</span><span>1</span><span>2</span><span>3</span><span>4</span><span>…</span><span>20</span><span>›</span></div>
</section>

<section class="share">
  <h4>SHARE THIS PAGE</h4>
  <div class="share-icons" aria-label="Share buttons"><span></span><span style="background:#3aa5dd"></span><span style="background:#1b74b0"></span><span style="background:#d64a37"></span></div>
</section>

<footer class="site-footer">
  <div class="footer-brand"><span class="brand-dot"></span><span>Verano Plum Cosmetics</span></div>
  <div class="quick-links">
    <h5>Quick Links</h5>
    <div>About Us</div><div>Blog</div><div>Sitemap</div>
  </div>
  <div class="tagline script">All Canadian <em>- All Inclusive</em></div>
  <div class="subscribe"><span>Subscribe to our newsletter</span><span class="field"></span><span class="go">Submit</span></div>
  <div class="footer-social" aria-label="Social links"><span></span><span></span></div>
</footer>
<div class="legal">
  <span>© 2024 Verano Plum Cosmetics. All Rights Reserved.<br>Terms · Privacy Policy · Contact Us</span>
  <span>Made in Canada with care for every skin tone</span>
  <span>English</span>
</div>

</body>
</html>
```